Business Card Design for Varnok Facility Services

We are looking for a Business Card Design for the Company "Varnok Facility Services."
Front side:
- Company Logo (small)
- Company Name, address, pohone, website and personal data.
- white background, for text e.g. company colors (blue or green like in the logo)
Please use following data:
Company data:
Varnok Facility Services Tulbrecht
Kirchmattweg 12
6331 Cham
www.varnok-fs.ch
Person data:
Ruben Tulbrecht
Geschäftsführer
+41 76 519 84 60
info@varnok-fs.ch
Back side:
could be colored in blue or green
please use a big logo sing and some smaller icons to say what is all beeing offered in facility services, like cleaning, maintenance cleaning
industrial cleaning, caretaking, gardening, disposal. There is no need for everyone of the icons if there are similar or an icon is standing for more of them.
Cleaning Service
colors to use:
blue: HEX 246BB0
green: HEX 52B33E

```html
<!DOCTYPE html>
<html lang="de">
<head>
<meta charset="utf-8">
<title>Varnok Facility Services – Visitenkarte</title>
<link rel="stylesheet" href="https://fonts.googleapis.com/css2?family=Montserrat:ital,wght@0,300;0,400;0,600;0,700;1,300;1,400;1,500&display=swap">
<style>
  :root{
    --blue:#246BB0;
    --green:#52B33E;
    --white:#ffffff;
    --stage:#E6E7E9;
  }
  *{box-sizing:border-box;margin:0;padding:0}
  html,body{width:1200px;height:1200px;overflow:hidden;background:var(--stage)}
  body{position:relative;font-family:"Montserrat",sans-serif}
  .card{position:absolute;left:202px;width:796px;height:455px;overflow:hidden;background:var(--white)}
  .card--front{top:137px}
  .card--back{top:609px;background:var(--blue)}
  .bands{position:absolute;inset:0;width:796px;height:455px}
  .abs{position:absolute}

  /* front */
  .brand-mark{left:0;right:0;top:58px;display:flex;align-items:center;justify-content:center;gap:10px}
  .brand-mark__dot{width:22px;height:22px;border-radius:50%;background:var(--green)}
  .brand-mark__name{font-weight:600;font-size:24px;color:var(--blue)}
  .company-line{left:0;right:0;top:138px;text-align:center;font-weight:700;font-size:21px;color:var(--green)}
  .row{display:flex;align-items:center;gap:14px;color:var(--white)}
  .row svg{width:19px;height:19px;flex:none}
  .person{left:55px;top:214px;font-size:27px}
  .person em{font-style:italic;font-weight:500}
  .role{left:160px;width:140px;top:258px;text-align:right;font-style:italic;font-weight:500;font-size:16px;color:var(--white)}
  .phone{left:55px;top:300px;font-size:27px}
  .email{left:55px;top:343px;font-size:27px}
  .divider{left:397px;top:231px;width:2px;height:139px;background:linear-gradient(var(--green),#e9f5e6 20%,#e9f5e6 80%,var(--green))}
  .address{left:453px;top:274px;align-items:flex-start;font-size:22px;line-height:25px}
  .address svg{margin-top:2px}
  .web-text{left:242px;width:310px;top:395px;text-align:center;font-size:24px;letter-spacing:3px;color:var(--blue)}

  /* back */
  .brand-mark--light{top:36px}
  .brand-mark--light .brand-mark__dot{background:var(--white)}
  .brand-mark--light .brand-mark__name{color:var(--white);font-size:30px}
  .company-line--light{top:101px;font-size:16px;color:var(--white)}
  .offers{left:75px;top:138px;font-style:italic;font-weight:300;font-size:29px;letter-spacing:3px;color:var(--white)}
  .offers-bar{height:4px;background:var(--white)}
  .service{width:97px;height:97px;border-radius:50%;background:var(--white);box-shadow:0 4px 14px rgba(0,0,0,.35);display:flex;align-items:center;justify-content:center}
  .service__art{width:70px;height:70px;border-radius:50%;background:radial-gradient(circle,#8fd17f,var(--green))}
</style>
</head>
<body>

<section class="card card--front" aria-label="Vorderseite">
  <svg class="bands" viewBox="0 0 796 455" aria-hidden="true">
    <polygon points="0,185 796,202 796,455 0,455" fill="var(--blue)"/>
    <polygon points="0,192 796,210 796,437 0,425" fill="var(--green)"/>
    <polygon points="0,425 796,437 796,444 0,433" fill="var(--white)"/>
    <g fill="var(--white)">
      <polygon points="212,396 226,396 212,421 198,421" />
      <polygon points="234,396 248,396 234,421 220,421" />
      <polygon points="252,396 552,396 538,421 240,421" />
      <polygon points="562,396 576,396 562,421 548,421" />
      <polygon points="584,396 598,396 584,421 570,421" />
    </g>
  </svg>

  <div class="abs brand-mark"><span class="brand-mark__dot"></span><span class="brand-mark__name">Varnok Facility Services</span></div>
  <div class="abs company-line">Varnok Facility Services Tulbrecht</div>

  <div class="abs row person">
    <svg viewBox="0 0 20 20"><circle cx="10" cy="10" r="10" fill="#fff"/><circle cx="10" cy="8" r="3.2" fill="var(--blue)"/><path d="M4.5 16.5a6 6 0 0 1 11 0z" fill="var(--blue)"/></svg>
    <span><em>Ruben</em> Tulbrecht</span>
  </div>
  <div class="abs role">Geschäftsführer</div>
  <div class="abs row phone">
    <svg viewBox="0 0 20 20"><circle cx="10" cy="10" r="10" fill="#fff"/><path d="M6.5 5.5l2 .3.8 2.2-1.2 1a7 7 0 0 0 3 3l1-1.2 2.2.8.3 2-1.5 1.2C9.5 14.6 5.4 10.5 5.3 7z" fill="var(--blue)"/></svg>
    <span>+41 76 519 84 60</span>
  </div>
  <div class="abs row email">
    <svg viewBox="0 0 20 20"><circle cx="10" cy="10" r="10" fill="#fff"/><rect x="5" y="6.5" width="10" height="7" rx="1" fill="none" stroke="var(--blue)" stroke-width="1.4"/><path d="M5.3 7l4.7 3.6L14.7 7" fill="none" stroke="var(--blue)" stroke-width="1.4"/></svg>
    <span>info@varnok-fs.ch</span>
  </div>

  <div class="abs divider"></div>

  <div class="abs row address">
    <svg viewBox="0 0 20 20"><circle cx="10" cy="10" r="10" fill="#fff"/><path d="M10 4a4.3 4.3 0 0 0-4.3 4.3c0 3.2 4.3 7.7 4.3 7.7s4.3-4.5 4.3-7.7A4.3 4.3 0 0 0 10 4z" fill="var(--blue)"/><circle cx="10" cy="8.3" r="1.8" fill="#fff"/></svg>
    <span>Kirchmattweg 12<br>6331 Cham</span>
  </div>

  <div class="abs web-text">www.varnok-fs.ch</div>
</section>

<section class="card card--back" aria-label="Rückseite">
  <svg class="bands" viewBox="0 0 796 455" aria-hidden="true">
    <polygon points="0,0 796,0 796,27 0,11" fill="var(--green)"/>
    <polygon points="0,4 796,19 796,25 0,10" fill="var(--white)"/>
    <polygon points="0,419 796,437 796,455 0,455" fill="var(--green)"/>
    <polygon points="0,419 796,437 796,443 0,425" fill="var(--white)"/>
  </svg>

  <div class="abs brand-mark brand-mark--light"><span class="brand-mark__dot"></span><span class="brand-mark__name">Varnok Facility Services</span></div>
  <div class="abs company-line company-line--light">Varnok Facility Services Tulbrecht</div>

  <div class="abs offers-bar" style="left:163px;top:134px;width:54px"></div>
  <div class="abs offers">We offers</div>
  <div class="abs offers-bar" style="left:83px;top:172px;width:81px"></div>

  <div class="abs service" style="left:105px;top:201px"><div class="service__art" role="img" aria-label="Pictogram: person cleaning floors"></div></div>
  <div class="abs service" style="left:300px;top:201px"><div class="service__art" role="img" aria-label="Pictogram: person doing maintenance work"></div></div>
  <div class="abs service" style="left:495px;top:201px"><div class="service__art" role="img" aria-label="Pictogram: ride-on industrial sweeper"></div></div>
  <div class="abs service" style="left:203px;top:304px"><div class="service__art" role="img" aria-label="Pictogram: caretaker assisting an elderly person"></div></div>
  <div class="abs service" style="left:398px;top:304px"><div class="service__art" role="img" aria-label="Pictogram: gardener with spade and tree"></div></div>
  <div class="abs service" style="left:592px;top:304px"><div class="service__art" role="img" aria-label="Pictogram: person disposing of waste"></div></div>
</section>

</body>
</html>
```